PowerPoint Design Project

We've recently updated our logo and we are in the processing of updating our web sites, business cards, letterhead, etc.

We're looking for a complete redesign of our Powerpoint template, which we have attached for reference.

Unfortunately our new web site is not released and is currently undergoing redesign so we can't send you a link to inspire.

Also attached here is our new logo.

Target Market(s)

Executives, Ph.D. scientists, researchers, venture capitalists, Board members

Industry/Entity Type

Business

```html
<!DOCTYPE html>
<html lang="en">
<head>
<meta charset="utf-8">
<title>Core Technologies 02 – Infrastructure</title>
<link href="https://fonts.googleapis.com/css2?family=Orbitron:wght@400&family=Source+Sans+3:ital,wght@0,400;1,400&display=swap" rel="stylesheet">
<style>
  :root {
    --sidebar-grey: #a7a7a7;
    --topband-grey: #7e7e7e;
    --header-blue-light: #5bbde6;
    --header-blue: #0a8fca;
    --accent-orange: #f7941d;
    --circle-blue: #1b8ac4;
    --circle-navy: #0c5a86;
    --badge-green: #1fd34f;
    --heading-blue: #1f5a85;
    --body-grey: #8a8a8a;
    --brand-blue: #1a8ac6;
    --ink-dark: #1d2a36;
    --white: #ffffff;
  }
  * { margin: 0; padding: 0; box-sizing: border-box; }
  html, body { width: 1200px; height: 900px; overflow: hidden; background: var(--white); }
  .slide {
    position: relative; width: 1200px; height: 900px; overflow: hidden;
    background: var(--white);
    font-family: "Source Sans 3", "Myriad Pro", sans-serif;
  }
  .top-band { position: absolute; left: 0; top: 0; width: 1200px; height: 30px; background: var(--topband-grey); }
  .sidebar { position: absolute; left: 0; top: 30px; width: 96px; height: 870px; background: var(--sidebar-grey); }
  .title-bar {
    position: absolute; left: 88px; top: 30px; width: 1112px; height: 72px;
    background: linear-gradient(90deg, var(--header-blue-light) 0%, var(--header-blue) 55%, var(--header-blue) 100%);
    box-shadow: 0 4px 6px rgba(0,0,0,0.18);
  }
  .slide-title {
    position: absolute; left: 47px; top: 14px;
    font-family: "Orbitron", sans-serif; font-weight: 400;
    font-size: 38px; letter-spacing: 5px; color: var(--white);
    transform: scaleX(0.88); transform-origin: left center;
    line-height: 44px;
  }
  .slide-title .section-number { color: var(--accent-orange); }

  .brand {
    position: absolute; left: 30px; top: 880px;
    transform: rotate(-90deg); transform-origin: left top;
    display: flex; align-items: center; gap: 8px;
    color: var(--brand-blue); font-size: 28px; font-weight: 400; white-space: nowrap;
  }
  .brand-dot { width: 26px; height: 26px; border-radius: 50%; background: var(--brand-blue); }

  .feature-graphic { position: absolute; left: 170px; top: 240px; width: 360px; height: 410px; }
  .feature-graphic svg { display: block; }
  .feature-label { font-family: "Source Sans 3", sans-serif; }

  .feature-copy {
    position: absolute; left: 648px; top: 276px; width: 457px;
    font-size: 20.5px; line-height: 33.6px; color: var(--body-grey);
    text-align: justify; hyphens: manual;
  }
  .feature-copy .lead { color: var(--heading-blue); }
</style>
</head>
<body>
<div class="slide">
  <div class="top-band"></div>
  <div class="sidebar"></div>
  <div class="title-bar">
    <h1 class="slide-title">CORE TECHNOLOGIES <span class="section-number">02</span></h1>
  </div>

  <div class="brand"><span class="brand-dot"></span><span>HelixPath</span></div>

  <div class="feature-graphic">
    <svg width="360" height="410" viewBox="170 240 360 410" xmlns="http://www.w3.org/2000/svg">
      <defs>
        <clipPath id="circle-clip"><circle cx="346" cy="416" r="171"/></clipPath>
        <linearGradient id="hardware-tone" x1="0" y1="0" x2="1" y2="1">
          <stop offset="0" stop-color="#9aa3ab"/>
          <stop offset="0.5" stop-color="#e9ecef"/>
          <stop offset="1" stop-color="#b7bec5"/>
        </linearGradient>
      </defs>
      <g clip-path="url(#circle-clip)">
        <rect x="170" y="240" width="360" height="108" fill="url(#hardware-tone)" role="img" aria-label="Close-up photo of server hardware components"/>
        <rect x="170" y="348" width="360" height="250" fill="var(--circle-blue)"/>
      </g>
      <text class="feature-label" x="213" y="332" font-size="27" font-style="italic" fill="var(--ink-dark)">Infrastructure</text>
      <circle cx="428" cy="348" r="32" fill="var(--badge-green)"/>
      <text class="feature-label" x="428" y="357" font-size="21" fill="var(--white)" text-anchor="middle">2</text>
      <g class="feature-label" font-size="20.5" fill="var(--white)" text-anchor="middle">
        <text x="346" y="419">Multiple, load-balanced head</text>
        <text x="346" y="448">nodes to service high-volume</text>
        <text x="346" y="476">user requests and interactions</text>
      </g>
      <circle cx="345" cy="575" r="66" fill="var(--circle-navy)"/>
      <g class="feature-label" font-size="20.5" font-style="italic" fill="var(--white)" text-anchor="middle">
        <text x="345" y="563">High</text>
        <text x="345" y="591">Performance</text>
      </g>
    </svg>
  </div>

  <p class="feature-copy"><span class="lead">High-performance Infrastructure:</span> A hosting architecture, designed in collaboration with Norvale Systems, with processing capacity of hundreds of genome sequences per month, and scaling to thousands per month. Features: multiple, load-balanced head nodes to service high-volume user requests and interactions, a stack of high-performance compute nodes to service highly-parallelized, sequence database comparisons, a storage solution scalable to petabytes, and fully redundant hardware and software for 24/7 availability.</p>
</div>
</body>
</html>
```